New business card for civil engineering company - "Keystone Audit"

We need a business card designed for our new structural engineering company.

The company name is "Keystone Audit" logo files attached.

We would like the following:
* Two-sided card
* Simple design

Information to be placed on the card:
Name - Marcus Dellow
Job Title - Director / Structural Engineer
Credentials - BEng(Hons), CPEng, CMengNZ, IntPE(NZ)
Email - marcus.dellow@keystoneaudit.co.nz
mobile - 0219364058
website - www.keystoneaudit.co.nz

```html
<!DOCTYPE html>
<html lang="en">
<head>
<meta charset="utf-8">
<title>Keystone Audit – Business Card</title>
<link rel="stylesheet" href="https://fonts.googleapis.com/css2?family=Lato:ital,wght@0,400;0,900;1,400&family=Exo+2:wght@500&display=swap">
<style>
  :root {
    --backdrop: #e8e5e1;
    --card-white: #ffffff;
    --card-dark: #3a3a3c;
    --brand-blue: #2a86c8;
    --text-dark: #333335;
    --text-light: #ffffff;
    --panel-light: #a6daf2;
    --panel-mid: #72c2ea;
    --panel-deep: #3a8dcc;
  }
  * { margin: 0; padding: 0; box-sizing: border-box; }
  html, body {
    width: 1200px; height: 900px; overflow: hidden;
    background: var(--backdrop);
  }
  .stage { position: relative; width: 1200px; height: 900px; }
  .card {
    position: absolute;
    width: 556px; height: 344px;
    overflow: hidden;
    box-shadow: 0 4px 10px rgba(0,0,0,0.25);
  }
  .card--front { left: 329px; top: 90px; background: var(--card-white); }
  .card--back { left: 331px; top: 469px; background: var(--card-dark); }

  .accent-panel {
    position: absolute; left: 333px; top: 0; width: 223px; height: 344px;
    background: linear-gradient(170deg, var(--panel-light) 0%, var(--panel-mid) 45%, var(--panel-deep) 100%);
  }

  .person { position: absolute; left: 30px; top: 52px; font-family: "Lato", sans-serif; color: var(--text-dark); }
  .person__name {
    font-weight: 900; font-size: 21px; letter-spacing: 0.6px;
    color: var(--brand-blue); text-transform: uppercase; line-height: 23px;
  }
  .person__role { font-size: 15.5px; line-height: 21px; }
  .person__credentials { font-size: 15.5px; font-style: italic; line-height: 21px; }

  .contacts {
    position: absolute; left: 30px; top: 223px;
    list-style: none; font-family: "Lato", sans-serif;
    font-size: 15.5px; color: var(--text-dark);
  }
  .contacts li { display: flex; align-items: center; height: 20px; }
  .contacts svg { width: 12px; height: 12px; margin-right: 5px; fill: var(--brand-blue); }

  .brand {
    position: absolute; left: 0; right: 0; top: 243px;
    text-align: center; color: var(--text-light);
    font-family: "Exo 2", sans-serif; font-weight: 500;
  }
  .brand__name { font-size: 27px; letter-spacing: 2.5px; text-transform: uppercase; line-height: 30px; }
  .brand__tagline { font-size: 11px; letter-spacing: 2.2px; text-transform: uppercase; margin-top: 2px; }
</style>
</head>
<body>
<main class="stage">
  <section class="card card--front">
    <div class="accent-panel" role="img" aria-label="Decorative blue geometric artwork panel"></div>

    <div class="person">
      <h1 class="person__name">Marcus Dellow</h1>
      <p class="person__role">Director / Structural Engineer</p>
      <p class="person__credentials">BEng(Hons), CPEng, CMengNZ, IntPE(NZ)</p>
    </div>

    <ul class="contacts">
      <li><svg viewBox="0 0 12 12"><path d="M3 0h6a1 1 0 0 1 1 1v10a1 1 0 0 1-1 1H3a1 1 0 0 1-1-1V1a1 1 0 0 1 1-1zm0 1.5v8h6v-8z"/></svg>0219364058</li>
      <li><svg viewBox="0 0 12 12"><path d="M0 2.5h12v7H0zM1 3.3v.4L6 7l5-3.3v-.4L6 6.5z"/></svg>marcus.dellow@keystoneaudit.co.nz</li>
      <li><svg viewBox="0 0 12 12"><circle cx="6" cy="6" r="4.5"/></svg>www.keystoneaudit.co.nz</li>
    </ul>
  </section>

  <section class="card card--back">
    <div class="brand">
      <p class="brand__name">Keystone Audit</p>
      <p class="brand__tagline">Peer Review Specialists</p>
    </div>
  </section>
</main>
</body>
</html>
```